Breezeway Comfort business cards design

Need a business card design for a Heating and Air Conditioning business. I need these items included.
Business name: Breezeway Comfort
Owner: Marcus Tollefsen
License # 2874590
Phone number # 555-382-4071
Email: breezewaycomfortair@mailvista.example
Sales
Service
Installation
Maintenance

Heating and Air Conditioning

Requirements
Must have
• Company name , license number , phone number , email

```html
<!DOCTYPE html>
<html lang="en">
<head>
<meta charset="utf-8">
<title>Breezeway Comfort – Business Cards</title>
<link rel="stylesheet" href="https://fonts.googleapis.com/css2?family=Montserrat:wght@400;500;600;700;800&display=swap">
<style>
  :root {
    --stage: #3a3a3c;
    --brand-blue: #1e46a0;
    --brand-orange: #f2822f;
    --brand-red: #e5405a;
    --ink: #1a1a1a;
    --paper: #ffffff;
  }
  * { box-sizing: border-box; margin: 0; padding: 0; }
  html, body { width: 1200px; height: 689px; overflow: hidden; }
  body {
    background: var(--stage);
    font-family: "Montserrat", sans-serif;
    position: relative;
  }
  .card {
    position: absolute;
    top: 190px;
    width: 540px;
    height: 309px;
    overflow: hidden;
    box-shadow: 0 14px 30px rgba(0,0,0,.45);
  }

  /* Front */
  .card-front { left: 40px; background: var(--brand-blue); }
  .front-lockup {
    position: absolute; left: 0; right: 0; top: 112px;
    display: flex; align-items: center; justify-content: center; gap: 18px;
  }
  .brand-dot {
    width: 62px; height: 62px; border-radius: 50%;
    background: var(--brand-orange);
    flex: none;
  }
  .front-text { display: flex; flex-direction: column; }
  .front-name {
    color: var(--paper); font-weight: 700; font-size: 34px;
    letter-spacing: 1px; text-transform: uppercase; line-height: 1;
  }
  .front-service {
    color: var(--brand-orange); font-weight: 600; font-size: 18px;
    letter-spacing: 5px; text-transform: uppercase; margin-top: 10px;
  }

  /* Back */
  .card-back { left: 620px; background: var(--paper); }
  .back-brand {
    position: absolute; left: 30px; top: 96px; width: 190px;
    display: flex; flex-direction: column; align-items: center; gap: 10px;
  }
  .back-brand .brand-dot { width: 44px; height: 44px; }
  .back-name {
    color: var(--brand-blue); font-weight: 700; font-size: 22px;
    text-transform: uppercase; text-align: center; line-height: 1.1;
  }
  .divider {
    position: absolute; left: 238px; top: 36px; width: 1.5px; height: 150px;
    background: var(--brand-blue);
  }
  .contact { position: absolute; left: 258px; top: 34px; }
  .person-name {
    font-weight: 800; font-size: 20px; text-transform: uppercase;
    color: var(--brand-red); line-height: 1.1;
  }
  .person-role { font-size: 12px; font-weight: 500; color: var(--ink); margin-top: 3px; }
  .contact-list { list-style: none; margin-top: 20px; }
  .contact-list li {
    display: flex; align-items: center; gap: 7px;
    font-size: 11.5px; color: var(--ink); line-height: 1.75;
  }
  .contact-list svg { width: 12px; height: 12px; fill: var(--brand-blue); flex: none; }
  .contact-list .no-icon { padding-left: 19px; }

  .service-band {
    position: absolute; left: 0; top: 236px; width: 410px; height: 36px;
    background: linear-gradient(90deg, var(--brand-red), var(--brand-orange));
    color: var(--paper); font-size: 13px; font-weight: 500;
    display: flex; align-items: center; justify-content: center;
  }
  .accent-block {
    position: absolute; right: 0; top: 200px; width: 78px; height: 36px;
    background: var(--brand-blue);
  }
  .accent-dot {
    position: absolute; left: 424px; top: 240px; width: 26px; height: 26px;
    border-radius: 50%; background: var(--brand-orange);
  }
</style>
</head>
<body>
  <section class="card card-front" aria-label="Business card front">
    <div class="front-lockup">
      <span class="brand-dot" aria-hidden="true"></span>
      <div class="front-text">
        <span class="front-name">Breezeway Comfort</span>
        <span class="front-service">Heating &amp; Air</span>
      </div>
    </div>
  </section>

  <section class="card card-back" aria-label="Business card back">
    <div class="back-brand">
      <span class="brand-dot" aria-hidden="true"></span>
      <span class="back-name">Breezeway Comfort</span>
    </div>
    <div class="divider" aria-hidden="true"></div>
    <div class="contact">
      <p class="person-name">Marcus Tollefsen</p>
      <p class="person-role">Managing Director</p>
      <ul class="contact-list">
        <li>
          <svg viewBox="0 0 24 24" aria-hidden="true"><path d="M6.6 10.8a15.1 15.1 0 0 0 6.6 6.6l2.2-2.2c.3-.3.7-.4 1-.2 1.1.4 2.3.6 3.6.6.6 0 1 .4 1 1V20c0 .6-.4 1-1 1A17 17 0 0 1 3 4c0-.6.4-1 1-1h3.5c.6 0 1 .4 1 1 0 1.3.2 2.5.6 3.6.1.3 0 .7-.2 1z"/></svg>
          # 555-382-4071
        </li>
        <li>
          <svg viewBox="0 0 24 24" aria-hidden="true"><path d="M2 5h20v14H2zm2 2v.5l8 5 8-5V7zm0 2.8V17h16V9.8l-8 5z"/></svg>
          breezewaycomfortair@mailvista.example
        </li>
        <li class="no-icon">License # 2874590</li>
      </ul>
    </div>
    <div class="accent-block" aria-hidden="true"></div>
    <div class="service-band">Sales, Service, Installation, Maintenance</div>
    <span class="accent-dot" aria-hidden="true"></span>
  </section>
</body>
</html>
```